Design for a real estate wev portal

Contents and features of the site
---------------------------------
Website in 5 languages: French, Dutch, English, German, Spanish.
English name of the site: Lantern Nest Place
Main purpose of the site:
- allow people to rent their house/ appartment for flatsharing purposes.
- help people wanting to find a room in flatsharing
- help people to find additional roommates for their flatsharing
Key interaction sequence:
1. I create a "group" of people who have common interest/hobbies
2. People who have the same interests/hobbies join my group
3. I look for a house/appartment to host my group
Website structure will be the following:
- Home
- Groups
-- Look for a group
--- Join a group
-- Create a group
- Properties
-- Look for a house/appartement
-- Apply
- Sales conditions
- Contact
- My account
-- My profile
-- My groups OR my properties
Your mission
------------
The client has no graphical guidelines, simply a logo (see attached).
We need a (responsive compliant) design for the following pages (we expect PSD's from you. No HTML nor CSS):
1. homepage (see example and wireframe attached)
2. properties search result list (see wireframe attached)
3. "detailed" form for properties
4. groups search result list
5. "detailed" form for groups
6. my account page
FOR THE COMPETITION step we only expect from you the design of first 2 screens.
Based on that, we will select the designer who will win the project, and will have to design the 4 remaining screens.
Target Market(s)
B2C
Industry/Entity Type
Real Estate
Number of Pages Required
5+ page
Look and feel
Each slider illustrates characteristics of the customer's brand and the style your logo design should communicate.

```html
<!DOCTYPE html>
<html lang="en">
<head>
<meta charset="utf-8">
<title>Lantern Nest Place – Home</title>
<link rel="stylesheet" href="https://fonts.googleapis.com/css2?family=Source+Sans+3:wght@400;600&display=swap">
<style>
  :root {
    --green: #6ab547;
    --teal: #1a9aa8;
    --teal-dark: #13919f;
    --ink: #2b2b2b;
    --white: #ffffff;
    --sky-top: #f2f2f0;
    --sky-mid: #e4e4e2;
    --city-low: #c9c6c2;
  }
  * { box-sizing: border-box; margin: 0; padding: 0; }
  html, body { width: 1200px; height: 545px; overflow: hidden; }
  body {
    font-family: "Source Sans 3", "Myriad Pro", sans-serif;
    color: var(--ink);
    background: var(--white);
    position: relative;
  }
  .site-header {
    position: absolute; left: 0; top: 0; width: 1200px; height: 99px;
    background: var(--white);
    box-shadow: 0 2px 6px rgba(0,0,0,0.12);
    z-index: 2;
  }
  .main-nav {
    position: absolute; left: 93px; top: 37px;
    display: flex; align-items: center;
    font-size: 14px;
  }
  .main-nav a {
    color: var(--ink); text-decoration: none;
    padding: 4px 6px; line-height: 18px; white-space: nowrap;
  }
  .main-nav a.is-active { background: var(--green); color: var(--white); padding: 4px 10px; margin-right: 3px; }
  .brand {
    position: absolute; left: 600px; top: 50px; transform: translate(-50%, -50%);
    display: flex; align-items: center; gap: 8px;
    font-size: 24px; font-weight: 600; color: var(--ink); white-space: nowrap;
  }
  .brand-dot { width: 12px; height: 12px; border-radius: 50%; background: var(--green); }
  .header-actions { position: absolute; top: 33px; left: 781px; display: flex; gap: 14px; }
  .btn {
    display: block; width: 155px; height: 35px; line-height: 35px;
    text-align: center; color: var(--white); text-decoration: none;
    font-size: 16px; font-weight: 600; letter-spacing: -0.2px;
    text-shadow: 0 1px 2px rgba(0,0,0,0.2);
  }
  .btn-login { background: var(--green); }
  .btn-account { background: var(--teal-dark); }
  .hero-backdrop {
    position: absolute; left: 0; top: 99px; width: 1200px; height: 446px;
    background: linear-gradient(180deg, var(--sky-top) 0%, var(--sky-mid) 45%, var(--city-low) 100%);
  }
  .choice-panel {
    position: absolute; top: 201px; width: 447px; height: 272px;
    color: var(--white); text-align: center;
  }
  .choice-panel.seekers { left: 129px; background: var(--green); }
  .choice-panel.owners { left: 622px; background: var(--teal); }
  .panel-title {
    font-size: 26px; font-weight: 400; margin-top: 24px; letter-spacing: -0.4px;
    white-space: nowrap;
    text-shadow: 0 1px 2px rgba(0,0,0,0.25);
  }
  .panel-options { position: absolute; left: 15px; top: 80px; display: flex; gap: 25px; }
  .option { width: 194px; }
  .option-photo { width: 194px; height: 115px; border: 1px solid rgba(255,255,255,0.9); }
  .option-label {
    margin-top: 11px; font-size: 16px; line-height: 21px;
    text-shadow: 0 1px 2px rgba(0,0,0,0.25);
  }
  .photo-keys { background: radial-gradient(circle at 35% 75%, #d9a25e 0%, #e8dccb 55%, #f4f1ea 100%); }
  .photo-friends { background: radial-gradient(circle at 50% 50%, #6a6a5a 0%, #3a3f30 55%, #25281f 100%); }
  .photo-landlord { background: radial-gradient(circle at 45% 55%, #8a7a6a 0%, #2a3348 45%, #1a2030 100%); }
  .photo-movers { background: radial-gradient(circle at 60% 55%, #e3c9a6 0%, #c79a6a 50%, #8e4a3a 100%); }
</style>
</head>
<body>
  <header class="site-header">
    <nav class="main-nav">
      <a href="#" class="is-active">Home</a>
      <a href="#">Groups</a>
      <a href="#">Properties</a>
      <a href="#">Sales conditions</a>
      <a href="#">Contact Us</a>
    </nav>
    <div class="brand"><span class="brand-dot"></span>Lantern Nest Place</div>
    <div class="header-actions">
      <a href="#" class="btn btn-login">SIGNUP/LOGIN</a>
      <a href="#" class="btn btn-account">MY ACCOUNT</a>
    </div>
  </header>

  <div class="hero-backdrop" role="img" aria-label="Soft blurred city skyline in pale grey tones"></div>

  <section class="choice-panel seekers">
    <h2 class="panel-title">SEARCHING FOR ACCOMMODATION</h2>
    <div class="panel-options">
      <div class="option">
        <div class="option-photo photo-keys" role="img" aria-label="Hand holding house keys in a bright room with moving boxes"></div>
        <p class="option-label">I want to rent a<br>room right now!</p>
      </div>
      <div class="option">
        <div class="option-photo photo-friends" role="img" aria-label="Group of friends lying in a circle on the grass"></div>
        <p class="option-label">I want to Join<br>a Group</p>
      </div>
    </div>
  </section>

  <section class="choice-panel owners">
    <h2 class="panel-title">I HAVE A HOUSE FOR RENT</h2>
    <div class="panel-options">
      <div class="option">
        <div class="option-photo photo-landlord" role="img" aria-label="Person in a suit holding a small model house and keys"></div>
        <p class="option-label">I want to advertise</p>
      </div>
      <div class="option">
        <div class="option-photo photo-movers" role="img" aria-label="Young flatmates moving in with cardboard boxes"></div>
        <p class="option-label">Why is flatsharing<br>interesting for me?</p>
      </div>
    </div>
  </section>
</body>
</html>
```